Luxury Business Card Design

We need a business card design for a law firm that look sophisticated and luxury

Target Market(s)

Australian legal markets

Industry/Entity Type

Legal

Contact Information for Business Card

Attached

Requirements
Must have
• Logo, head office address on front side and 2 other addresses on the back side.
Nice to have
• Please see below our current business card. Need something more sophisticated and luxury feel

```html
<!DOCTYPE html>
<html lang="en">
<head>
<meta charset="utf-8">
<title>Ashford Lawyers – Business Cards</title>
<link href="https://fonts.googleapis.com/css2?family=Lato:wght@400;700;900&display=swap" rel="stylesheet">
<style>
  :root {
    --backdrop: #1d1c1d;
    --forest: #1b3124;
    --forest-deep: #12231a;
    --gold: #c9a45c;
    --ink: #14261c;
    --paper: #ffffff;
    --muted: #e8e6df;
  }
  * { box-sizing: border-box; margin: 0; padding: 0; }
  html, body { width: 1200px; height: 939px; overflow: hidden; }
  body {
    background: var(--backdrop);
    font-family: "Lato", sans-serif;
    position: relative;
  }
  .card {
    position: absolute;
    width: 580px;
    height: 350px;
    border-radius: 22px;
    border-bottom: 4px solid var(--gold);
    border-left: 2px solid var(--gold);
    overflow: hidden;
  }

  /* Front: office locations */
  .card--offices {
    left: 60px; top: 80px;
    background: linear-gradient(160deg, var(--forest) 0%, var(--forest-deep) 100%);
    color: var(--muted);
  }
  .brand {
    position: absolute; top: 96px; left: 0; right: 0;
    text-align: center;
    font-weight: 700; font-size: 36px; letter-spacing: 5px;
    color: var(--paper); line-height: 1.1;
  }
  .offices {
    position: absolute; left: 30px; right: 26px; bottom: 36px;
    display: grid; grid-template-columns: 1fr 1fr 1fr;
    align-items: start;
  }
  .office { padding: 0 14px; font-size: 12.5px; line-height: 1.45; white-space: nowrap; }
  .office + .office { border-left: 1px solid var(--gold); }
  .office__city {
    color: var(--gold); font-weight: 900; font-size: 15px; letter-spacing: .5px;
    margin-bottom: 2px;
  }
  .office__phone {
    display: flex; align-items: center; gap: 6px;
    font-weight: 700; color: var(--paper); margin-top: 3px;
  }
  .office__phone svg { width: 11px; height: 11px; }

  /* Back: personal details */
  .card--person {
    left: 560px; top: 500px;
    background: var(--paper);
    color: var(--ink);
  }
  .mini-brand {
    position: absolute; top: 30px; right: 30px;
    font-weight: 700; font-size: 12px; letter-spacing: 2px; color: var(--ink);
  }
  .person {
    position: absolute; right: 308px; top: 148px; text-align: right; white-space: nowrap;
  }
  .person__name { font-weight: 900; font-size: 32px; letter-spacing: .5px; line-height: 1.05; }
  .person__role { color: var(--gold); font-size: 17px; margin-top: 4px; }
  .person__quals { color: var(--gold); font-size: 15px; }
  .divider {
    position: absolute; left: 290px; top: 86px; width: 2px; height: 176px;
    background: var(--ink);
  }
  .contacts {
    position: absolute; left: 316px; top: 88px; list-style: none;
    font-size: 15px; line-height: 1.4; white-space: nowrap;
  }
  .contacts li { display: flex; gap: 10px; align-items: flex-start; }
  .contacts li + li { margin-top: 2px; }
  .contacts .address { margin-bottom: 8px; }
  .contacts svg { width: 13px; height: 13px; margin-top: 4px; flex: none; }
  .tagline {
    position: absolute; bottom: 32px; left: 0; right: 0; text-align: center;
    font-weight: 900; font-size: 13px; letter-spacing: 4px; color: var(--ink);
  }
</style>
</head>
<body>

<section class="card card--offices">
  <div class="brand">ASHFORD LAWYERS</div>
  <div class="offices">
    <div class="office">
      <div class="office__city">MELBOURNE</div>
      Ashford Lawyers<br>Level 12, 48 Bay Lane<br>Melbourne, VIC 3000
      <div class="office__phone"><svg viewBox="0 0 24 24"><path fill="#c9a45c" d="M6.6 10.8a15 15 0 0 0 6.6 6.6l2.2-2.2a1 1 0 0 1 1-.25 11.4 11.4 0 0 0 3.6.57 1 1 0 0 1 1 1V20a1 1 0 0 1-1 1A17 17 0 0 1 3 4a1 1 0 0 1 1-1h3.5a1 1 0 0 1 1 1c0 1.25.2 2.45.57 3.57a1 1 0 0 1-.25 1z"/></svg>+61 03 5550 1842</div>
    </div>
    <div class="office">
      <div class="office__city">SYDNEY</div>
      Level 9, Meridian Building<br>22 Kent Row<br>Parramatta, NSW 2150
      <div class="office__phone"><svg viewBox="0 0 24 24"><path fill="#c9a45c" d="M6.6 10.8a15 15 0 0 0 6.6 6.6l2.2-2.2a1 1 0 0 1 1-.25 11.4 11.4 0 0 0 3.6.57 1 1 0 0 1 1 1V20a1 1 0 0 1-1 1A17 17 0 0 1 3 4a1 1 0 0 1 1-1h3.5a1 1 0 0 1 1 1c0 1.25.2 2.45.57 3.57a1 1 0 0 1-.25 1z"/></svg>+61 02 5550 7316</div>
    </div>
    <div class="office">
      <div class="office__city">PERTH</div>
      Level 18, Crest Tower<br>75 Riverside Parade<br>Perth, WA 6000
      <div class="office__phone"><svg viewBox="0 0 24 24"><path fill="#c9a45c" d="M6.6 10.8a15 15 0 0 0 6.6 6.6l2.2-2.2a1 1 0 0 1 1-.25 11.4 11.4 0 0 0 3.6.57 1 1 0 0 1 1 1V20a1 1 0 0 1-1 1A17 17 0 0 1 3 4a1 1 0 0 1 1-1h3.5a1 1 0 0 1 1 1c0 1.25.2 2.45.57 3.57a1 1 0 0 1-.25 1z"/></svg>+61 08 5550 2960</div>
    </div>
  </div>
</section>

<section class="card card--person">
  <div class="mini-brand">ASHFORD LAWYERS</div>
  <div class="person">
    <div class="person__name">DANIEL MERCER</div>
    <div class="person__role">Director &amp; Principal Solicitor</div>
    <div class="person__quals">MPA, Juris Doctor</div>
  </div>
  <div class="divider"></div>
  <ul class="contacts">
    <li class="address"><svg viewBox="0 0 24 24"><path fill="#c9a45c" d="M12 2a7 7 0 0 0-7 7c0 5 7 13 7 13s7-8 7-13a7 7 0 0 0-7-7zm0 9.5A2.5 2.5 0 1 1 12 6.5a2.5 2.5 0 0 1 0 5z"/></svg><span>Level 3, Ashford House<br>210 Linden Terrace<br>Spring Hill, QLD 4000</span></li>
    <li><svg viewBox="0 0 24 24"><path fill="#c9a45c" d="M6.6 10.8a15 15 0 0 0 6.6 6.6l2.2-2.2a1 1 0 0 1 1-.25 11.4 11.4 0 0 0 3.6.57 1 1 0 0 1 1 1V20a1 1 0 0 1-1 1A17 17 0 0 1 3 4a1 1 0 0 1 1-1h3.5a1 1 0 0 1 1 1c0 1.25.2 2.45.57 3.57a1 1 0 0 1-.25 1z"/></svg>+61 7 5550 4418</li>
    <li><svg viewBox="0 0 24 24"><rect x="6" y="2" width="12" height="20" rx="2" fill="none" stroke="#c9a45c" stroke-width="2.5"/><circle cx="12" cy="18" r="1.3" fill="#c9a45c"/></svg>+61 0491 570 226</li>
    <li><svg viewBox="0 0 24 24"><rect x="2" y="5" width="20" height="14" rx="1.5" fill="#c9a45c"/><path d="M3 6l9 7 9-7" fill="none" stroke="#fff" stroke-width="1.8"/></svg>daniel@ashfordlawyers.com.au</li>
    <li><svg viewBox="0 0 24 24"><circle cx="12" cy="12" r="10" fill="#c9a45c"/><path d="M2 12h20M12 2c3 3 3 17 0 20M12 2c-3 3-3 17 0 20" fill="none" stroke="#fff" stroke-width="1.4"/></svg>ashfordlawyers.com.au</li>
  </ul>
  <div class="tagline">CLEAR ADVICE. STRONG OUTCOMES. ALWAYS.</div>
</section>

</body>
</html>
```